Vale Lanternwick Needs a new website!

We need a four page website for a new company based in San Francisco. We help companies connect better with their clients, employees, and vendors by implementing collaborative technology.
Similar Websites
Brindle Oarsmen - http://www.brindleoarsmen.example/
Mossquill - http://www.mossquill.example/ - I don't like the the rotating window or the pictures of people. I like the icons used to go to the next pages.
Color Combos
Blues and Yellows - http://www.huepairings.example/hue-sets/96/HueSet96.html
We prefer graphics over the actual pictures of people in the header. Pictures of people working together in the text is fine.
Web Page Layout
Index
Cloud Advisory Services
Email Everywhere
CRM Implementation
For detailed copy please see this link https://pages.fernlodge.example/a/tinkerwrensf.example/document/d/7KxTqP2mZvLw9RbHs4-_n-YcEuJdAoNfgXtVkQr5mwbe/edit
Industry/Entity Type
It Company

```html
<!DOCTYPE html>
<html lang="en">
<head>
<meta charset="utf-8">
<title>Vale Lanternwick — Cloud Solutions for the Modern Workforce</title>
<link rel="stylesheet" href="https://fonts.googleapis.com/css2?family=Nunito:wght@300;400;600;700;800&family=Open+Sans:ital,wght@0,400;0,600;0,700;1,400&display=swap">
<style>
:root{
  --blue:#2a66b8;
  --blue-dark:#1f4f95;
  --blue-light:#3b7fd0;
  --yellow:#f7c900;
  --yellow-deep:#efbd00;
  --ink:#333;
  --grey:#8a8a8a;
  --grey-light:#efefef;
  --footer:#353535;
  --white:#fff;
}
*{box-sizing:border-box;margin:0;padding:0}
html,body{width:1200px;height:3203px;overflow:hidden}
body{position:relative;background:var(--white);font-family:"Open Sans",Arial,sans-serif;color:var(--ink)}
.abs{position:absolute}
.heading{font-family:"Nunito",Arial,sans-serif}

/* header */
.site-header{position:absolute;left:0;top:0;width:1200px;height:117px;background:var(--white)}
.brand{position:absolute;left:115px;top:34px;display:flex;align-items:center;gap:12px}
.brand-dot{width:46px;height:46px;border-radius:50%;background:var(--blue)}
.brand-name{font-family:"Nunito",sans-serif;font-weight:800;font-size:30px;color:var(--blue);letter-spacing:.2px}
.search{position:absolute;left:563px;top:38px;width:367px;height:37px;border:1px solid #ddd;display:flex;align-items:center;padding:0 12px;font-size:13px;color:#aaa}
.search svg{position:absolute;right:12px;top:9px}
.register{position:absolute;left:953px;top:38px;width:112px;height:37px;background:var(--yellow);color:var(--white);font-size:12px;font-weight:700;display:flex;align-items:center;justify-content:center}

/* nav */
.main-nav{position:absolute;left:0;top:117px;width:1200px;height:64px;background:linear-gradient(#3677c8,#2760ae)}
.main-nav a{position:absolute;top:0;height:64px;line-height:64px;color:var(--white);text-decoration:none;font-family:"Nunito",sans-serif;font-weight:600;font-size:17px;text-align:center}
.main-nav a.active{background:var(--yellow)}

/* hero */
.hero{position:absolute;left:0;top:181px;width:1200px;height:656px;overflow:hidden}
.hero-visual{position:absolute;inset:0;background:linear-gradient(100deg,#5d6e80 0%,#4a5b70 35%,#31435c 60%,#2a3a52 100%)}
.hero-title{position:absolute;left:115px;top:145px;font-family:"Nunito",sans-serif;font-weight:700;font-size:88px;color:var(--yellow);line-height:1}
.hero-sub{position:absolute;left:115px;top:250px;font-family:"Nunito",sans-serif;font-weight:400;font-size:42px;color:var(--white);line-height:1.25}
.hero-arrow{position:absolute;top:228px;width:42px;height:42px;border-radius:50%;border:2px solid var(--white);background:rgba(0,0,0,.35)}
.hero-features{position:absolute;left:0;top:536px;width:1200px;height:120px;background:rgba(40,44,52,.72)}
.feature{position:absolute;top:30px;display:flex;gap:18px}
.feature-icon{width:60px;height:60px;border-radius:50%;background:var(--yellow);flex:none;display:flex;align-items:center;justify-content:center}
.feature h3{font-family:"Nunito",sans-serif;font-weight:400;font-size:24px;color:var(--white);line-height:1;margin-top:-2px}
.feature p{font-size:12px;color:#ccc;line-height:1.5;margin-top:8px;width:210px}

/* what we do */
.section-title{position:absolute;left:0;width:1200px;text-align:center;font-family:"Nunito",sans-serif;font-weight:800;font-size:34px;color:var(--blue)}
.section-intro{position:absolute;left:0;width:1200px;text-align:center;font-style:italic;font-size:15px;color:var(--grey);line-height:26px}
.step{position:absolute;top:1036px;width:200px;text-align:center}
.step-ring{width:128px;height:128px;margin:0 auto;border-radius:50%;background:var(--white);border:6px solid #eee;box-shadow:0 0 0 1px #ddd inset;display:flex;align-items:center;justify-content:center}
.step-ring.on{background:var(--blue);border-color:#e6e6e6}
.step h4{font-family:"Nunito",sans-serif;font-weight:700;font-size:18px;color:#222;margin-top:26px}
.step p{font-size:12.5px;color:#666;line-height:20px;margin-top:8px}
.step .more{display:block;font-size:11.5px;font-weight:700;color:var(--blue);margin-top:12px}

/* advisory band */
.advisory{position:absolute;left:0;top:1328px;width:1200px;height:483px}
.advisory-bg{position:absolute;inset:0;background:linear-gradient(135deg,#f8cf10 0%,#f5c400 50%,#f8cd0a 100%)}
.advisory h2{position:absolute;left:0;top:50px;width:1200px;text-align:center;color:var(--white);font-family:"Nunito",sans-serif;font-weight:300;font-size:62px}
.advisory h2 b{font-weight:800;font-size:86px}
.advisory h3{position:absolute;left:0;top:150px;width:1200px;text-align:center;color:var(--white);font-family:"Nunito",sans-serif;font-weight:300;font-size:40px}
.advisory p{position:absolute;left:170px;top:222px;width:860px;text-align:center;color:var(--white);font-size:16.5px;line-height:32px}
.btn-outline{position:absolute;left:455px;top:369px;width:288px;height:58px;border:2px solid var(--white);color:var(--white);font-family:"Nunito",sans-serif;font-weight:700;font-size:21px;display:flex;align-items:center;justify-content:center}

/* clients */
.clients{position:absolute;left:0;top:1811px;width:1200px;height:224px;background:var(--grey-light)}
.clients h2{position:absolute;left:115px;top:64px;font-family:"Nunito",sans-serif;font-weight:700;font-size:40px;color:var(--blue)}
.clients .kicker{position:absolute;left:115px;top:122px;font-family:"Nunito",sans-serif;font-size:22px;color:#444}
.client{position:absolute;top:32px;width:240px}
.avatar{width:77px;height:77px;border-radius:50%;border:3px solid var(--white);box-shadow:0 0 0 1px #ccc;margin-left:0}
.client h5{font-size:14px;font-weight:600;color:#333;margin-top:14px}
.client .role{font-size:12px;color:var(--yellow-deep);margin-top:2px}
.client p{font-size:12px;color:#666;line-height:18px;margin-top:2px}

/* services */
.service{position:absolute;top:2205px;width:289px;text-align:center}
.service-img{width:289px;height:208px;border:4px solid var(--white);box-shadow:0 0 0 1px #ddd}
.service h4{font-family:"Nunito",sans-serif;font-weight:700;font-size:17px;color:var(--blue);margin-top:26px}
.service p{font-size:14px;color:#777;line-height:22px;margin-top:12px;padding:0 20px}
.chev{position:absolute}

/* partners */
.quote{position:absolute;left:0;top:2655px;width:1200px;text-align:center;font-style:italic;font-size:18px;color:#777;line-height:26px}
.quote-rule{position:absolute;left:255px;top:2627px;width:690px;height:1px;background:#e3e3e3}
.partner{position:absolute;top:2764px;font-family:"Nunito",sans-serif;font-weight:800;font-size:24px;color:#222}

/* footer */
.site-footer{position:absolute;left:0;top:2850px;width:1200px;height:353px;background:var(--footer);color:var(--white)}
.foot-h{position:absolute;top:38px;font-family:"Nunito",sans-serif;font-weight:700;font-size:16px;color:var(--yellow)}
.foot-h::after{content:"";position:absolute;left:0;top:28px;width:180px;height:1px;background:#555}
.foot-list{position:absolute;top:88px;list-style:none;font-size:12.5px;line-height:21px;color:#eee}
.foot-text{position:absolute;font-size:12px;line-height:19px;color:#eee}
.email-field{position:absolute;left:625px;top:148px;width:215px;height:32px;border:1px solid #777;font-size:11px;color:#aaa;padding:8px}
.subscribe{position:absolute;left:625px;top:195px;width:118px;height:34px;background:var(--yellow);color:var(--white);font-weight:700;font-size:14px;display:flex;align-items:center;justify-content:center}
.tag{position:absolute;height:28px;border:1px solid #ccc;font-size:11px;color:#eee;display:flex;align-items:center;justify-content:center}
.contact-tab{position:absolute;left:1158px;top:110px;width:42px;height:116px;background:var(--blue);border-radius:6px 0 0 6px;display:flex;align-items:center;justify-content:center}
.contact-tab span{writing-mode:vertical-rl;font-size:12px;font-weight:700;letter-spacing:4px;color:var(--white)}
.social{position:absolute;top:303px;width:28px;height:28px;border-radius:50%;background:var(--blue-light)}
.legal{position:absolute;left:700px;top:309px;font-size:11.5px;color:#eee}
.legal a{color:var(--yellow);text-decoration:none}
</style>
</head>
<body>

<header class="site-header">
  <div class="brand"><span class="brand-dot"></span><span class="brand-name">Vale Lanternwick</span></div>
  <div class="search">Enter any keyword
    <svg width="20" height="20" viewBox="0 0 20 20"><circle cx="8" cy="8" r="6" fill="none" stroke="#2a66b8" stroke-width="2.5"/><line x1="12.5" y1="12.5" x2="18" y2="18" stroke="#2a66b8" stroke-width="3"/></svg>
  </div>
  <div class="register">REGISTER HERE</div>
</header>

<nav class="main-nav">
  <a class="active" style="left:115px;width:105px">Home</a>
  <a style="left:241px;width:190px">Cloud Advisory Services</a>
  <a style="left:466px;width:146px">Email Everywhere</a>
  <a style="left:646px;width:172px">CRM Implementation</a>
  <a style="left:852px;width:106px">What We Do</a>
  <a style="left:992px;width:78px">About Us</a>
</nav>

<section class="hero">
  <div class="hero-visual" role="img" aria-label="Businessman in a suit holding his hands around a small white cloud"></div>
  <div class="hero-title">Cloud</div>
  <div class="hero-sub">Solutions for the<br>Modern Workforce</div>
  <svg class="hero-arrow" style="left:-2px" viewBox="0 0 42 42"><polyline points="24,12 15,21 24,30" fill="none" stroke="#fff" stroke-width="3"/></svg>
  <svg class="hero-arrow" style="left:1130px" viewBox="0 0 42 42"><polyline points="18,12 27,21 18,30" fill="none" stroke="#fff" stroke-width="3"/></svg>
  <div class="hero-features">
    <div class="feature" style="left:115px">
      <div class="feature-icon"><svg width="30" height="20" viewBox="0 0 30 20"><path d="M8 19h16a5 5 0 0 0 0-10 8 8 0 0 0-15-2 6 6 0 0 0-1 12z" fill="#fff"/></svg></div>
      <div><h3>Cloud Advisory</h3><p>Forward- thinking organizations would like to be more collaborative....</p></div>
    </div>
    <div class="feature" style="left:444px">
      <div class="feature-icon"><svg width="28" height="20" viewBox="0 0 28 20"><rect x="1" y="1" width="26" height="18" fill="none" stroke="#fff" stroke-width="2.5"/><polyline points="1,1 14,11 27,1" fill="none" stroke="#fff" stroke-width="2.5"/></svg></div>
      <div><h3>Email Everywhere</h3><p>Drive forward your business with inn ovative solutions for the ...</p></div>
    </div>
    <div class="feature" style="left:775px">
      <div class="feature-icon"><svg width="26" height="26" viewBox="0 0 26 26"><rect x="2" y="5" width="18" height="18" rx="3" fill="none" stroke="#fff" stroke-width="2.5"/><line x1="10" y1="16" x2="23" y2="3" stroke="#fff" stroke-width="3"/></svg></div>
      <div><h3>CRM Solutions</h3><p>CRMs (Customer Relationship Manag ement) can be complex....</p></div>
    </div>
  </div>
</section>

<h2 class="section-title" style="top:872px">What We Do</h2>
<p class="section-intro" style="top:937px">We challenge the status quo by providing unique insights, emerging strategies and proven best practices.<br>Our unwavering focus is on customer satisfaction.&nbsp; Our services include</p>

<div class="step" style="left:92px">
  <div class="step-ring on"><svg width="44" height="44" viewBox="0 0 44 44"><circle cx="22" cy="22" r="18" fill="none" stroke="#fff" stroke-width="3"/><circle cx="22" cy="22" r="11" fill="none" stroke="#fff" stroke-width="3"/><circle cx="22" cy="22" r="4" fill="#fff"/><line x1="22" y1="22" x2="22" y2="42" stroke="#2a66b8" stroke-width="6"/><line x1="22" y1="24" x2="22" y2="42" stroke="#fff" stroke-width="3"/></svg></div>
  <h4>Strategy</h4><p>Forward- thinking organiza<br>like to be more collabor</p><span class="more">READ MORE</span>
</div>
<div class="step" style="left:291px">
  <div class="step-ring"><svg width="40" height="40" viewBox="0 0 40 40"><path d="M20 4l7 12h-5l-2-4-5 9-5-3zM36 26l-7 12-3-5 4-7-10 0 0-6 14 0zM4 26l7 12 3-5-4-7 6-10-5-3z" fill="#2a66b8"/></svg></div>
  <h4>Migration</h4><p>Forward- thinking organiza<br>like to be more collabor</p><span class="more">READ MORE</span>
</div>
<div class="step" style="left:489px">
  <div class="step-ring"><svg width="44" height="44" viewBox="0 0 44 44"><circle cx="22" cy="22" r="19" fill="none" stroke="#2a66b8" stroke-width="4"/><circle cx="22" cy="22" r="11" fill="none" stroke="#2a66b8" stroke-width="4"/><circle cx="22" cy="22" r="4" fill="#2a66b8"/></svg></div>
  <h4>Implementation</h4><p>Forward- thinking organiza<br>like to be more collabor</p><span class="more">READ MORE</span>
</div>
<div class="step" style="left:686px">
  <div class="step-ring"><svg width="40" height="40" viewBox="0 0 40 40"><path d="M6 12h9a5 5 0 1 1 10 0h9v9a5 5 0 1 0 0 10v7H25a5 5 0 1 0-10 0H6v-9a5 5 0 1 1 0-10z" fill="#2a66b8"/></svg></div>
  <h4>Integration</h4><p>Forward- thinking organiza<br>like to be more collabor</p><span class="more">READ MORE</span>
</div>
<div class="step" style="left:886px">
  <div class="step-ring"><svg width="48" height="34" viewBox="0 0 48 34"><path d="M12 32h24a9 9 0 0 0 0-18 13 13 0 0 0-25-2A10 10 0 0 0 12 32z" fill="#2a66b8"/><polyline points="18,20 24,14 30,20" fill="none" stroke="#fff" stroke-width="3"/><line x1="24" y1="15" x2="24" y2="27" stroke="#fff" stroke-width="3"/></svg></div>
  <h4>Adoption &amp; CM</h4><p>Forward- thinking organiza<br>like to be more collabor</p><span class="more">READ MORE</span>
</div>

<section class="advisory">
  <div class="advisory-bg" role="img" aria-label="Yellow background with a faint faceted polygon texture"></div>
  <h2><b>Cloud</b> Advisory Services</h2>
  <h3>Universal Access</h3>
  <p>Success in the cloud begins with a sound strategy.&nbsp; Start with a strong evaluation process.&nbsp; Then determine the right solution, proper implementation strategy and change management method. With the right transition you could recognize the benefits of the cloud:</p>
  <div class="btn-outline">MORE INFORMATION</div>
</section>

<section class="clients">
  <h2>Clients</h2>
  <div class="kicker">Say About us</div>
  <svg class="abs" style="left:213px;top:170px" width="34" height="14" viewBox="0 0 34 14"><polyline points="9,2 3,7 9,12" fill="none" stroke="#999" stroke-width="3"/><polyline points="25,2 31,7 25,12" fill="none" stroke="#999" stroke-width="3"/></svg>
  <div class="client" style="left:303px">
    <div class="avatar" role="img" aria-label="Portrait of a client" style="background:linear-gradient(#c9a27f,#8a5a3a)"></div>
    <h5>Natoque penatibus</h5><div class="role">JR Holloway city name</div>
    <p>Location: rewr ksu Titel vanhLorem ipsum<br>dolor sit amet, consectetur ad pisci elit.</p>
  </div>
  <div class="client" style="left:570px">
    <div class="avatar" role="img" aria-label="Portrait of a client" style="background:linear-gradient(#8fb0d0,#c8a070)"></div>
    <h5>Natoque penatibus</h5><div class="role">JR Holloway city name</div>
    <p>Location: rewr ksu Titel vanhLorem ipsum<br>dolor sit amet, consectetur ad pisci elit.</p>
  </div>
  <div class="client" style="left:845px">
    <div class="avatar" role="img" aria-label="Portrait of a client" style="background:linear-gradient(#8fb0d0,#c8a070)"></div>
    <h5>Natoque penatibus</h5><div class="role">JR Holloway city name</div>
    <p>Location: rewr ksu Titel vanhLorem ipsum<br>dolor sit amet, consectetur ad pisci elit.</p>
  </div>
</section>

<h2 class="section-title" style="top:2065px">Our services</h2>
<p class="section-intro" style="top:2118px">We challenge the status quo by providing unique insights, emerging strategies and proven best practices.<br>Our unwavering focus is on customer satisfaction.&nbsp; Our services include</p>

<svg class="chev" style="left:80px;top:2308px" width="16" height="26" viewBox="0 0 16 26"><polyline points="13,2 3,13 13,24" fill="none" stroke="#aaa" stroke-width="3"/></svg>
<svg class="chev" style="left:1082px;top:2308px" width="16" height="26" viewBox="0 0 16 26"><polyline points="3,2 13,13 3,24" fill="none" stroke="#aaa" stroke-width="3"/></svg>

<div class="service" style="left:115px">
  <div class="service-img" role="img" aria-label="Hand reaching toward a glowing cloud with network lines" style="background:linear-gradient(135deg,#0d2c5a,#2f7cc0 55%,#9fd0f0)"></div>
  <h4>Training</h4><p>How can life sciences organizations improve their service operations? This eBook provides insight into</p>
</div>
<div class="service" style="left:455px">
  <div class="service-img" role="img" aria-label="Open hand beneath floating digital icons" style="background:linear-gradient(135deg,#061a33,#1b5d92 55%,#67b6e6)"></div>
  <h4>Deployment</h4><p>How can life sciences organizations improve their service operations? This eBook provides insight into</p>
</div>
<div class="service" style="left:773px">
  <div class="service-img" role="img" aria-label="Laptop in use under a blue sky with clouds" style="background:linear-gradient(160deg,#4d8fd6,#a8cdef 55%,#3a4a5c)"></div>
  <h4>Project management</h4><p>How can life sciences organizations improve their service operations? This eBook provides insight into</p>
</div>

<div class="quote-rule"></div>
<svg class="abs" style="left:218px;top:2650px" width="26" height="20" viewBox="0 0 26 20"><path d="M2 18V10L8 2h3L8 10h4v8zM14 18V10l6-8h3l-3 8h4v8z" fill="#ccc"/></svg>
<p class="quote">Our art is challenging the status quo, challenging our clients and creating<br>solutions that can change the way that people work forever</p>
<svg class="abs" style="left:948px;top:2680px" width="26" height="20" viewBox="0 0 26 20"><path d="M24 2v8l-6 8h-3l3-8h-4V2zM12 2v8l-6 8H3l3-8H2V2z" fill="#ccc"/></svg>

<svg class="chev" style="left:115px;top:2768px" width="14" height="24" viewBox="0 0 14 24"><polyline points="12,2 3,12 12,22" fill="none" stroke="#999" stroke-width="3"/></svg>
<svg class="chev" style="left:1052px;top:2768px" width="14" height="24" viewBox="0 0 14 24"><polyline points="2,2 11,12 2,22" fill="none" stroke="#999" stroke-width="3"/></svg>
<span class="partner" style="left:163px">Corvane</span>
<span class="partner" style="left:270px">Halvery</span>
<span class="partner" style="left:432px">Pellstone</span>
<span class="partner" style="left:576px">Quorith</span>
<span class="partner" style="left:758px">Dunmere</span>
<span class="partner" style="left:888px">Ostwick Partner</span>

<footer class="site-footer">
  <h4 class="foot-h" style="left:115px">About Us</h4>
  <ul class="foot-list" style="left:115px">
    <li>Home</li><li>About Us</li><li>Services</li><li>Success Stories</li><li>News &amp; Events</li><li>Patners</li><li>Contact us</li>
  </ul>

  <h4 class="foot-h" style="left:355px">Conatct Us</h4>
  <div class="foot-text" style="left:355px;top:85px;font-size:13px">Northgate Ireland</div>
  <div class="foot-text" style="left:362px;top:106px;font-size:11px;line-height:17px">Dublin +353 01 555 0142<br>Galway +353 091 555 0187<br>UK +44 20 5550 1296</div>
  <div class="foot-text" style="left:360px;top:175px;font-size:10.5px;line-height:16px;font-weight:700">SkyLedger<br>StreamKeep<br>ShiftHarbor</div>

  <h4 class="foot-h" style="left:625px">Newsletter</h4>
  <div class="foot-text" style="left:625px;top:92px;font-size:11.5px">Sign up with your name and email<br>to get updates fresh updates.</div>
  <div class="email-field">Email:</div>
  <div class="subscribe">SUBSCRIBE</div>

  <h4 class="foot-h" style="left:918px">Usefull Tags</h4>
  <div class="tag" style="left:918px;top:97px;width:66px">Some</div>
  <div class="tag" style="left:998px;top:97px;width:66px">Are teh</div>
  <div class="tag" style="left:918px;top:133px;width:40px">is</div>
  <div class="tag" style="left:965px;top:133px;width:99px">Lorem ipsum</div>
  <div class="tag" style="left:918px;top:170px;width:66px">Some</div>
  <div class="tag" style="left:998px;top:170px;width:66px">Are teh</div>
  <div class="tag" style="left:918px;top:207px;width:40px">is</div>
  <div class="tag" style="left:965px;top:207px;width:99px">Lorem ipsum</div>

  <div class="contact-tab"><span>CONTACT</span></div>

  <span class="social" style="left:115px" aria-label="Social profile"></span>
  <span class="social" style="left:151px" aria-label="Social profile"></span>
  <span class="social" style="left:187px" aria-label="Social profile"></span>
  <span class="social" style="left:223px" aria-label="Social profile"></span>
  <div class="legal">© CopyrightVale Lanternwick Ltd | <a>Privacy Policy</a> | <a>Term of Use</a></div>
</footer>

</body>
</html>
```